Northbound's green Wagon Van Decal

Good day,
I am looking for a decal or wrap for my work van. The name of the Business is Northbound’s Green Wagon, and we are a van rental company with a provided driver. We offer transport, delivery and expediting services to our customers.
The Van is a 2024 Vexa Cargoline 3400 159in wb ext. and its red.
I do not want a fully 360 top to bottom van decal just the region in green on both side of the van and in the back for the decal. See attached.
The following is text information that needs to be added on the decal.
- Name of the Business is Northbound’s Green Wagon
- Company motto: Your buddy behind the wheel
- Van Rental with driver
- Evenings and weekends.
The costumer can contact us by:
Email: Rosedale@northboundsgreenwagon.com
Phone or Text at: 555-274-9061
Keep in mind that the van is RED. If I cannot Invision what your wrap will look like on the Van there’s a high chance it won’t be chosen.
Thank you for your time.
Updates
Low design quality
Good day,
I have change the requirement of the project. it should be a lot more manageable and foster more creativity from designer.
Please have a look at the revise brief if you're interested.
Industry/Entity Type
Moving business
Look and feel
Each slider illustrates characteristics of the customer's brand and the style your logo design should communicate.

```html
<!DOCTYPE html>
<html lang="en">
<head>
<meta charset="utf-8">
<title>Northbound's Green Wagon – Van Decal</title>
<link href="https://fonts.googleapis.com/css2?family=Poppins:wght@400;600;700;800;900&display=swap" rel="stylesheet">
<style>
  :root {
    --bg: #2b2b2b;
    --red: #c4121f;
    --red-deep: #8e1017;
    --red-bright: #e3262f;
    --ink: #1a1a1a;
    --paper: #f3f3f3;
    --paper-shade: #dcdcdc;
    --white: #ffffff;
  }
  * { box-sizing: border-box; margin: 0; padding: 0; }
  html, body { width: 1039px; height: 1200px; overflow: hidden; background: var(--bg); }
  body { position: relative; font-family: "Poppins", sans-serif; font-weight: 800; text-transform: uppercase; }

  .decal { position: absolute; overflow: hidden; background: linear-gradient(180deg, var(--paper), var(--paper-shade)); }
  .decal .swoosh { position: absolute; inset: 0; width: 100%; height: 100%; }
  .decal > *:not(.swoosh) { position: absolute; }

  .brand { display: flex; align-items: center; gap: 10px; color: var(--ink); font-weight: 800; line-height: 1.15; text-transform: none; }
  .brand-dot { flex: none; border-radius: 50%; background: var(--red); }

  .accent { color: var(--red-bright); }
  .dark { color: var(--ink); }

  /* side panel */
  .decal-side { left: 30px; top: 296px; width: 980px; height: 178px; }
  .decal-side .brand { left: 24px; top: 50px; width: 190px; font-size: 17px; }
  .decal-side .brand-dot { width: 34px; height: 34px; }
  .decal-side .motto { left: 362px; top: 16px; color: var(--white); line-height: 1; }
  .decal-side .motto-main { font-size: 30px; }
  .decal-side .motto-sub { font-size: 19px; margin-top: 2px; }
  .decal-side .service { left: 640px; top: 16px; color: var(--white); font-size: 17px; }
  .decal-side .hours-pill { left: 622px; top: 50px; width: 290px; height: 70px; border-radius: 10px; background: var(--ink); border: 2px solid var(--red); color: var(--white); text-align: center; padding-top: 9px; }
  .decal-side .hours-pill .hours { font-size: 17px; }
  .decal-side .hours-pill .website { font-size: 11px; margin-top: 4px; }
  .decal-side .contact-label { left: 226px; top: 106px; background: var(--ink); color: var(--white); font-size: 11px; padding: 3px 10px; border-radius: 3px; }
  .decal-side .phone { left: 224px; top: 128px; font-size: 38px; letter-spacing: 0.5px; line-height: 1.1; }
  .decal-side .email { left: 520px; top: 136px; width: 430px; height: 28px; background: var(--red); color: var(--white); font-size: 15px; line-height: 28px; text-align: center; border-radius: 3px; }

  /* back panel */
  .decal-back { left: 80px; top: 564px; width: 880px; height: 340px; }
  .decal-back .brand { left: 56px; top: 140px; width: 280px; font-size: 24px; }
  .decal-back .brand-dot { width: 52px; height: 52px; }
  .decal-back .motto { right: 50px; top: 12px; text-align: right; color: var(--white); line-height: 1; }
  .decal-back .motto-main { font-size: 40px; }
  .decal-back .motto-sub { font-size: 28px; margin-top: 4px; }
  .decal-back .service { right: 50px; top: 96px; background: var(--ink); color: var(--white); font-size: 19px; padding: 4px 14px; border-radius: 4px; }
  .decal-back .service span { font-weight: 400; }
  .decal-back .hours { right: 50px; top: 140px; color: var(--white); font-size: 22px; text-align: right; line-height: 1.2; }
  .decal-back .contact-badge { left: 372px; top: 84px; width: 132px; height: 132px; border-radius: 50%; background: var(--red); border: 3px solid var(--ink); color: var(--white); display: flex; align-items: center; justify-content: center; text-align: center; font-size: 19px; line-height: 1.05; }
  .decal-back .contact-badge span { transform: rotate(-14deg); }
  .decal-back .phone { right: 50px; top: 222px; font-size: 56px; letter-spacing: 0.5px; line-height: 1.1; }
  .decal-back .email { right: 50px; top: 292px; width: 480px; height: 32px; background: var(--red); color: var(--white); font-size: 18px; line-height: 32px; text-align: center; border-radius: 3px; }
</style>
</head>
<body>

<section class="decal decal-side" aria-label="Side panel decal">
  <svg class="swoosh" viewBox="0 0 980 178" preserveAspectRatio="none" aria-hidden="true">
    <path d="M205,0 C250,70 330,108 470,108 C640,108 780,80 980,96 L980,116 C780,98 640,126 470,124 C320,122 240,80 190,0 Z" fill="var(--ink)"/>
    <path d="M215,0 C260,68 340,100 470,100 C640,100 780,72 980,88 L980,0 Z" fill="var(--red)"/>
  </svg>
  <div class="brand"><span class="brand-dot"></span>Northbound’s Green Wagon</div>
  <div class="motto">
    <div class="motto-main">Your <span class="dark">Buddy</span></div>
    <div class="motto-sub">Behind the Wheel</div>
  </div>
  <div class="service">Van Rental with Driver</div>
  <div class="hours-pill">
    <div class="hours"><span class="accent">Evenings and</span> Weekends</div>
    <div class="website">northboundsgreenwagon.com</div>
  </div>
  <div class="contact-label">Phone or Text at</div>
  <div class="phone"><span class="accent">555-274-</span><span class="dark">9061</span></div>
  <div class="email">Rosedale@northboundsgreenwagon.com</div>
</section>

<section class="decal decal-back" aria-label="Rear doors decal">
  <svg class="swoosh" viewBox="0 0 880 340" preserveAspectRatio="none" aria-hidden="true">
    <path d="M0,46 C90,8 200,0 300,18 C400,40 460,120 540,168 C620,208 760,200 880,190 L880,212 C760,222 610,230 528,184 C450,140 390,66 300,40 C200,16 90,24 0,64 Z" fill="var(--ink)"/>
    <path d="M150,0 L880,0 L880,190 C760,200 620,208 540,168 C460,120 400,40 300,18 C250,6 200,0 150,0 Z" fill="var(--red)"/>
  </svg>
  <div class="brand"><span class="brand-dot"></span>Northbound’s Green Wagon</div>
  <div class="motto">
    <div class="motto-main">Your <span class="dark">Buddy</span></div>
    <div class="motto-sub">Behind the Wheel</div>
  </div>
  <div class="service">Van Rental <span>with Driver</span></div>
  <div class="hours">Evenings and<br>Weekends</div>
  <div class="contact-badge"><span>Phone<br>or<br>Text at</span></div>
  <div class="phone"><span class="accent">555-274-</span><span class="dark">9061</span></div>
  <div class="email">Rosedale@northboundsgreenwagon.com</div>
</section>

</body>
</html>
```